Judge Whitlock's Mill Jubilee BBQ

We need a flyer promoting a BBQ, music, and community conversation campaign event that is happening in conjunction with a larger community event "Mill Jubilee" It is for the Re Elect Judge Peter Whitlock campaign, all are invited. We would like the design to be very Americana, and feature the Judge's name at the top or near the top. Play with the slogans "Shade Trees and Sweet Tea, BBQ and Music, Time to Visit and Talk" and "Judge Whitlocks Mill Jubilee BBQ Bash: Music, Politics and Community"

```html
<!DOCTYPE html>
<html lang="en">
<head>
<meta charset="utf-8">
<title>Judge Whitlock's Mill Jubilee BBQ Bash</title>
<link rel="stylesheet" href="https://fonts.googleapis.com/css2?family=Oswald:wght@400;700&family=Merriweather:wght@700&family=Kaushan+Script&display=swap">
<style>
  :root {
    --backdrop: #253650;
    --navy: #2c4872;
    --red: #d42027;
    --red-dark: #9b1b22;
    --cream: #fefadf;
    --sketch-tone: #e9e6d6;
  }
  * { margin: 0; padding: 0; box-sizing: border-box; }
  html, body { width: 1200px; height: 1200px; overflow: hidden; }
  body { background: var(--backdrop); position: relative; }

  .flyer {
    position: absolute; left: 180px; top: 60px;
    width: 840px; height: 1080px;
    background: var(--cream);
    box-shadow: 0 4px 18px rgba(0,0,0,.35);
  }
  .flyer > * { position: absolute; }

  .speed-stripes { top: 38px; width: 176px; height: 90px; }
  .speed-stripes--left { left: 34px; }
  .speed-stripes--right { right: 35px; }

  .invite-line {
    top: 36px; left: 0; width: 100%;
    text-align: center;
    font-family: 'Oswald', sans-serif; font-weight: 400;
    font-size: 40px; color: var(--navy); line-height: 56px;
  }

  .name-ribbon { left: 130px; top: 120px; width: 571px; height: 106px; }
  .name-ribbon__text {
    left: 0; top: 120px; width: 840px; height: 87px;
    display: flex; align-items: center; justify-content: center;
    font-family: 'Merriweather', serif; font-weight: 700;
    font-size: 38px; color: var(--cream); white-space: nowrap;
  }

  .event-title {
    top: 264px; left: 0; width: 100%;
    text-align: center; white-space: nowrap;
    font-family: 'Oswald', sans-serif; font-weight: 700;
    font-size: 76px; line-height: 96px; color: var(--navy);
  }

  .rule { height: 1.5px; background: var(--navy); left: 153px; width: 533px; }
  .rule--top { top: 381px; }
  .rule--bottom { top: 471px; }

  .tagline {
    top: 392px; left: 0; width: 100%;
    text-align: center; white-space: nowrap;
    font-family: 'Kaushan Script', cursive;
    font-size: 52px; line-height: 70px; color: var(--red);
  }

  .event-date {
    top: 500px; left: 0; width: 100%;
    display: flex; align-items: center; justify-content: center; gap: 24px;
    font-family: 'Oswald', sans-serif; font-weight: 400;
    font-size: 46px; line-height: 62px; color: var(--navy);
  }
  .event-date svg { width: 26px; height: 26px; }

  .double-rule { height: 13px; border-top: 4px solid var(--navy); border-bottom: 4px solid var(--navy); }
  .double-rule--upper-left { top: 596px; left: 34px; width: 280px; }
  .double-rule--upper-right { top: 596px; left: 539px; width: 266px; }
  .double-rule--lower-left { top: 918px; left: 34px; width: 215px; }
  .double-rule--lower-right { top: 918px; left: 590px; width: 215px; }

  .amenities {
    top: 583px; left: 0; width: 100%;
    text-align: center;
    font-family: 'Oswald', sans-serif; font-weight: 400;
    font-size: 60px; line-height: 72px; color: var(--navy);
  }

  .sketch { border-radius: 12px; background: radial-gradient(circle at 50% 50%, #dcdcd6, var(--sketch-tone) 75%); }
  .sketch--tea { left: 34px; top: 629px; width: 236px; height: 264px; }
  .sketch--grill { left: 614px; top: 635px; width: 191px; height: 261px; }

  .closing-band {
    left: 0; top: 982px; width: 100%; height: 52px;
    background: var(--red);
    display: flex; align-items: center; justify-content: center; gap: 30px;
  }
  .closing-band__text {
    font-family: 'Merriweather', serif; font-weight: 700;
    font-size: 36px; color: var(--cream); line-height: 52px;
  }
  .closing-band svg { width: 68px; height: 8px; }
</style>
</head>
<body>
<main class="flyer">
  <svg class="speed-stripes speed-stripes--left" viewBox="0 0 176 90" aria-hidden="true">
    <g fill="var(--red)">
      <rect x="0" y="0" width="176" height="5"/>
      <rect x="0" y="17" width="149" height="5"/>
      <rect x="0" y="34" width="122" height="5"/>
      <rect x="0" y="50" width="96" height="5"/>
      <rect x="0" y="67" width="69" height="5"/>
      <rect x="0" y="83" width="42" height="5"/>
    </g>
  </svg>
  <svg class="speed-stripes speed-stripes--right" viewBox="0 0 176 90" aria-hidden="true">
    <g fill="var(--red)">
      <rect x="0" y="0" width="176" height="5"/>
      <rect x="27" y="17" width="149" height="5"/>
      <rect x="54" y="34" width="122" height="5"/>
      <rect x="80" y="50" width="96" height="5"/>
      <rect x="107" y="67" width="69" height="5"/>
      <rect x="134" y="83" width="42" height="5"/>
    </g>
  </svg>

  <p class="invite-line">All are Invited to</p>

  <svg class="name-ribbon" viewBox="0 0 571 106" aria-hidden="true">
    <polygon points="0,20 96,20 96,106 0,106 22,63" fill="var(--red)"/>
    <polygon points="35,86 96,86 96,106" fill="var(--red-dark)"/>
    <polygon points="571,20 475,20 475,106 571,106 549,63" fill="var(--red)"/>
    <polygon points="536,86 475,86 475,106" fill="var(--red-dark)"/>
    <rect x="35" y="0" width="501" height="87" fill="var(--navy)"/>
    <rect x="35" y="9" width="501" height="1" fill="var(--red)"/>
    <rect x="35" y="76" width="501" height="1" fill="var(--red)"/>
  </svg>
  <h2 class="name-ribbon__text">Judge Peter Whitlock's</h2>

  <h1 class="event-title">MILL JUBILEE BBQ BASH</h1>

  <div class="rule rule--top"></div>
  <p class="tagline">Pickin' Grillin' &amp; Politickin</p>
  <div class="rule rule--bottom"></div>

  <p class="event-date">
    <svg viewBox="0 0 24 24" aria-hidden="true"><polygon fill="var(--red)" points="12,1 15,9 23,9 16.5,14 19,22 12,17 5,22 7.5,14 1,9 9,9"/></svg>
    <span>June 8th from 10am - 2pm</span>
    <svg viewBox="0 0 24 24" aria-hidden="true"><polygon fill="var(--red)" points="12,1 15,9 23,9 16.5,14 19,22 12,17 5,22 7.5,14 1,9 9,9"/></svg>
  </p>

  <div class="double-rule double-rule--upper-left"></div>
  <div class="double-rule double-rule--upper-right"></div>

  <div class="sketch sketch--tea" role="img" aria-label="Engraved sketch of a tea kettle, a cup on a saucer and mint leaves"></div>

  <p class="amenities">Unlimited<br>Shade Trees<br>and<br>Sweet Tea,<br>BBQ and Music</p>

  <div class="sketch sketch--grill" role="img" aria-label="Engraved sketch of a grill basket with steaks and rising smoke"></div>

  <div class="double-rule double-rule--lower-left"></div>
  <div class="double-rule double-rule--lower-right"></div>

  <div class="closing-band">
    <svg viewBox="0 0 68 8" aria-hidden="true"><polygon fill="var(--cream)" points="0,4 68,0 68,8"/></svg>
    <span class="closing-band__text">Time to Visit and Talk</span>
    <svg viewBox="0 0 68 8" aria-hidden="true"><polygon fill="var(--cream)" points="68,4 0,0 0,8"/></svg>
  </div>
</main>
</body>
</html>
```